Back Pain

Need a flyer similar to the attached draft. This is to be handed out to prospective patients. Note that Sketch Hive has already designed the logo. If you need a copy please contact me

```html
<!DOCTYPE html>
<html lang="en">
<head>
<meta charset="utf-8">
<title>Spinal Ease Clinic – Tech Neck Flyer</title>
<link rel="stylesheet" href="https://fonts.googleapis.com/css2?family=Bebas+Neue&family=Poppins:wght@400;600&display=swap">
<style>
  :root {
    --bg: #dcdcdc;
    --ink: #000000;
    --green: #8cc63f;
    --blue: #1a75c4;
    --white: #ffffff;
    --shadow: #1a1f24;
  }
  * { box-sizing: border-box; margin: 0; padding: 0; }
  html, body { width: 1200px; height: 967px; overflow: hidden; background: var(--bg); }
  .flyer {
    position: absolute; left: 282px; top: 33px; width: 636px; height: 900px;
    background: var(--ink); overflow: hidden; color: var(--white);
    font-family: "Bebas Neue", "Oswald", sans-serif;
  }
  .title {
    position: absolute; left: 30px; top: 28px; width: 576px;
    color: var(--green); font-size: 78px; line-height: 1; text-align: center; letter-spacing: 1px;
  }
  .figure-area {
    position: absolute; left: 40px; top: 120px; width: 190px; height: 520px;
    border-radius: 90px 90px 30px 30px;
    background: linear-gradient(180deg, #15191d 0%, #0b0d10 100%);
    box-shadow: 0 0 6px rgba(120,130,140,0.35);
  }
  .symptoms { position: absolute; left: 120px; top: 140px; list-style: none; }
  .symptoms li {
    height: 32px; margin-bottom: 10px; padding: 0 12px;
    background: var(--blue); color: var(--green);
    font-size: 26px; line-height: 34px; text-align: right; border-radius: 0 4px 4px 0;
  }
  .chart-caption {
    position: absolute; left: 410px; top: 140px; width: 210px;
    color: var(--green); font-size: 17px; line-height: 1.05;
  }
  .chart { position: absolute; left: 400px; top: 200px; }
  .chart text { font-family: "Bebas Neue", sans-serif; }
  .device-stat {
    position: absolute; left: 400px; top: 386px; width: 230px;
    display: flex; align-items: center; gap: 10px;
  }
  .device-stat .badge { width: 60px; height: 60px; flex: none; display: block; }
  .device-stat p { font-size: 16px; line-height: 1.05; }
  .device-stat strong { font-size: 24px; font-weight: 400; }
  .device-stat .accent { color: var(--blue); }
  .statement {
    position: absolute; left: 20px; top: 474px; width: 596px;
    font-size: 46px; line-height: 44px; text-align: right;
  }
  .statement .accent { color: var(--blue); }
  .divider {
    position: absolute; left: 170px; top: 676px; width: 440px;
    border-top: 2px dotted #5a7f2e;
  }
  .practitioner {
    position: absolute; left: 30px; top: 690px; width: 590px;
    font-family: "Poppins", sans-serif; font-size: 22px; line-height: 1.3; color: var(--green); text-align: right;
  }
  .practitioner b { font-weight: 600; }
  .brand { position: absolute; left: 28px; top: 782px; display: flex; align-items: center; gap: 8px; }
  .brand .dot { width: 34px; height: 34px; border-radius: 50%; background: var(--blue); }
  .brand span { font-family: "Poppins", sans-serif; font-weight: 600; font-size: 15px; color: var(--blue); }
  .offer { position: absolute; left: 230px; top: 772px; display: flex; align-items: flex-start; }
  .offer .num { font-size: 86px; line-height: 0.85; }
  .offer .unit { display: flex; flex-direction: column; font-size: 34px; line-height: 0.9; margin-left: 2px; }
  .offer-note {
    position: absolute; left: 370px; top: 780px; width: 250px;
    font-family: "Poppins", sans-serif; font-size: 13px; line-height: 1.4;
  }
  .offer-note .url { color: var(--green); font-weight: 600; }
  .offer-note .fine { display: block; margin-top: 4px; font-size: 11px; text-align: right; }
  .offer-note .fine b { font-weight: 600; }
  .edge-band {
    position: absolute; left: 0; bottom: 0; width: 100%; height: 16px;
    background: linear-gradient(90deg, var(--green), var(--blue));
  }
</style>
</head>
<body>
<main class="flyer">
  <h1 class="title">Spinal Ease Clinic</h1>

  <div class="figure-area" role="img" aria-label="Dark silhouette of a man walking while looking down at his phone"></div>

  <ul class="symptoms">
    <li style="width:190px;margin-left:80px">Headaches</li>
    <li style="width:170px;margin-left:60px">Neck Pain</li>
    <li style="width:230px;margin-left:40px">Shoulder Pain</li>
    <li style="width:170px;margin-left:20px">Back Pain</li>
    <li style="width:240px;margin-left:0">Arm &amp; Hand Pain</li>
    <li style="width:140px;margin-left:-20px">Sciatica</li>
  </ul>

  <p class="chart-caption">As the head tilts forward,<br>more force is placed<br>on the spine</p>
  <svg class="chart" width="230" height="170" viewBox="0 0 230 170" role="img" aria-label="Bar chart of pressure on the spine by degree of forward head tilt">
    <rect x="6" y="0" width="40" height="40" fill="#1a1f24" rx="20" role="img" aria-label="Small head silhouette"/>
    <rect x="6" y="106" width="28" height="24" fill="#1a75c4"/>
    <rect x="42" y="76" width="28" height="54" fill="#1a75c4"/>
    <rect x="78" y="50" width="28" height="80" fill="#1a75c4"/>
    <rect x="114" y="32" width="28" height="98" fill="#1a75c4"/>
    <rect x="150" y="10" width="28" height="120" fill="#1a75c4"/>
    <g fill="#8cc63f" font-size="18" text-anchor="middle">
      <text x="20" y="125">12</text><text x="56" y="95">27</text><text x="92" y="69">40</text>
      <text x="128" y="51">49</text><text x="164" y="29">60</text>
    </g>
    <g fill="#ffffff" font-size="13" text-anchor="middle">
      <text x="20" y="145">0°</text><text x="56" y="145">15°</text><text x="92" y="145">30°</text>
      <text x="128" y="145">45°</text><text x="164" y="145">60°</text>
      <text x="92" y="163">Degrees of forward head tilt</text>
    </g>
    <text x="205" y="130" fill="#ffffff" font-size="12" transform="rotate(-90 205 130)">Pressure on spine (lbs)</text>
  </svg>

  <div class="device-stat">
    <svg class="badge" viewBox="0 0 70 70" aria-hidden="true">
      <path d="M35 0 A35 35 0 0 0 35 70 Z" fill="#8cc63f"/>
      <path d="M35 0 A35 35 0 0 1 35 70 Z" fill="#1a75c4"/>
      <rect x="25" y="16" width="20" height="38" rx="3" fill="none" stroke="#ffffff" stroke-width="3"/>
      <circle cx="35" cy="49" r="2" fill="#ffffff"/>
    </svg>
    <p>The average person spends<br><strong><span class="accent">8-11</span> hours per day</strong><br>using electronic devices</p>
  </div>

  <p class="statement">
    Chiropractic care <span class="accent">can help</span><br>
    <span class="accent">correct and prevent these problems</span><br>
    <span class="accent">by</span> restoring and maintaining<br>
    proper alignment <span class="accent">of the</span> neck
  </p>

  <div class="divider"></div>

  <p class="practitioner"><b>Dr Daniel Hartley</b> Now in<br>Eastwood Bay at 42 Harbour ST - Marina Suites</p>

  <div class="brand"><div class="dot"></div><span>SPINAL EASE CLINIC</span></div>

  <div class="offer"><span class="num">50</span><span class="unit"><span>%</span><span>OFF</span></span></div>

  <p class="offer-note">Initial Consultation if you book online at <span class="url">www.spinaleaseclinic.com.au</span>
    <span class="fine">*Choose <b>“TECH NECK”</b> Option</span></p>

  <div class="edge-band"></div>
</main>
</body>
</html>
```